Dietitian needs awesome business card

I need a contemporary design that's eye catching but professional.
My card is to given to doctors, specialists and patients alike.
I manage patients with chronic diseases
I have uploaded my logo and current business card, I would also like the other Registered Clinical Nutritionist logo incorporated into the design

Target Market(s)

Doctors, specialists and patients

Industry/Entity Type

Healthcare

Contact Information for Business Card

www.brindlecovenutrition.com.au
Ph: 0427 516 903
Fax: 6482 7315
email: marcus.k.wellfare@quorvamail.com
Space on the back of the card with: Appointment date, Appointment time and appointment location

Font styles to use
Serif

Colors
fbee3e
876aae
ffc214

Requirements
Must have
• My Logo
• Registered Clinical Nutritionist Logo
• My 4 locations - Fernhollow Medical Centre, North Kelby Health, Ashcourt Medical, Pinebrook Doctors Surgery
Nice to have
• I like the colours in my current business card

```html
<!DOCTYPE html>
<html lang="en">
<head>
<meta charset="utf-8">
<title>Brindlecove Nutrition &amp; Dietetics — Business Card</title>
<link href="https://fonts.googleapis.com/css2?family=PT+Serif:ital,wght@0,400;0,700;1,400&display=swap" rel="stylesheet">
<style>
  :root {
    --page: #ecebe7;
    --card: #ffffff;
    --blue: #0b7cc8;
    --blue-deep: #0a57a3;
    --green: #8cc63f;
    --lime: #d6e61c;
    --grey-text: #5d5f62;
    --rule: #b9bcbf;
    --badge: #e8822a;
  }
  * { box-sizing: border-box; margin: 0; padding: 0; }
  html, body { width: 1200px; height: 1023px; overflow: hidden; }
  body {
    background: var(--page);
    font-family: "PT Serif", Georgia, serif;
    position: relative;
  }
  .card {
    position: absolute;
    left: 220px;
    width: 760px;
    height: 450px;
    background: var(--card);
    border-radius: 22px;
    overflow: hidden;
    box-shadow: 0 6px 18px rgba(0,0,0,.18);
  }
  .card--front { top: 41px; }
  .card--back { top: 532px; }
  .card__bands { position: absolute; inset: 0; width: 100%; height: 100%; }

  /* Front */
  .brand {
    position: absolute; left: 48px; top: 70px;
    display: flex; align-items: center; gap: 16px;
  }
  .brand__dot {
    width: 58px; height: 58px; border-radius: 50%;
    background: var(--blue);
  }
  .brand__name {
    color: var(--blue);
    font-size: 30px; font-weight: 400; line-height: 1.1;
  }
  .person {
    position: absolute; left: 120px; top: 178px;
    color: var(--blue);
    font-size: 28px; font-weight: 700;
    padding-bottom: 10px;
    border-bottom: 1px solid var(--rule);
    width: 340px;
  }
  .contacts {
    position: absolute; left: 120px; top: 236px;
    list-style: none;
    color: var(--grey-text);
    font-size: 19px;
  }
  .contacts li { display: flex; align-items: center; gap: 12px; height: 30px; }
  .contacts svg { width: 18px; height: 18px; fill: var(--blue); flex: none; }

  /* Back */
  .appointment__title {
    position: absolute; left: 210px; top: 40px;
    color: var(--blue-deep);
    font-size: 34px; letter-spacing: 2px;
  }
  .field {
    position: absolute; left: 210px;
    display: flex; align-items: flex-end; gap: 10px;
    color: var(--grey-text); font-size: 21px; width: 500px;
  }
  .field::after {
    content: ""; flex: 1; border-bottom: 2px dotted var(--grey-text);
    margin-bottom: 6px;
  }
  .field--date { top: 112px; }
  .field--time { top: 162px; }
  .location__title {
    position: absolute; left: 210px; top: 222px;
    color: var(--green); font-size: 26px;
  }
  .location__list {
    position: absolute; left: 210px; top: 272px;
    list-style: none;
    display: grid; grid-template-columns: 255px 205px; row-gap: 14px;
    color: var(--blue); font-size: 17px;
  }
  .location__list li { display: flex; align-items: center; gap: 10px; white-space: nowrap; }
  .checkbox {
    width: 18px; height: 18px; border: 1.5px solid var(--grey-text); flex: none;
  }
  .badge {
    position: absolute; right: 30px; bottom: 46px;
    width: 96px; height: 60px; background: var(--badge);
  }
</style>
</head>
<body>

<section class="card card--front" aria-label="Card front">
  <svg class="card__bands" viewBox="0 0 760 450" aria-hidden="true">
    <defs>
      <linearGradient id="swoosh" x1="0" y1="0" x2="1" y2="1">
        <stop offset="0" stop-color="#8cc63f"/>
        <stop offset=".55" stop-color="#d6e61c"/>
        <stop offset="1" stop-color="#8cc63f"/>
      </linearGradient>
    </defs>
    <path d="M395,0 C555,0 615,150 598,255 C580,360 430,398 250,404 L0,410 L0,450 L760,450 L760,0 Z" fill="#c9cbcd"/>
    <path d="M410,0 C565,0 628,150 610,258 C592,365 440,406 255,414 L0,418 L0,450 L760,450 L760,0 Z" fill="url(#swoosh)"/>
    <path d="M610,0 L760,0 L760,330 C735,200 700,80 610,0 Z" fill="#0a57a3"/>
    <path d="M0,428 C60,430 110,440 140,450 L0,450 Z" fill="#0b7cc8"/>
  </svg>

  <div class="brand">
    <span class="brand__dot"></span>
    <span class="brand__name">Brindlecove<br>Nutrition &amp; Dietetics</span>
  </div>

  <h1 class="person">Marcus Kellaway</h1>

  <ul class="contacts">
    <li><svg viewBox="0 0 24 24"><rect x="3" y="8" width="18" height="12" rx="2"/><rect x="7" y="3" width="10" height="6"/></svg>6482 7315</li>
    <li><svg viewBox="0 0 24 24"><path d="M6 2h4l2 5-3 2a12 12 0 0 0 6 6l2-3 5 2v4a2 2 0 0 1-2 2A18 18 0 0 1 4 4a2 2 0 0 1 2-2z"/></svg>0427 516 903</li>
    <li><svg viewBox="0 0 24 24"><path d="M2 5h20v14H2z M2 5l10 8 10-8" stroke="#fff" stroke-width="1.5"/></svg>marcus.k.wellfare@quorvamail.com</li>
    <li><svg viewBox="0 0 24 24"><circle cx="12" cy="12" r="10"/><path d="M2 12h20M12 2c4 4 4 16 0 20M12 2c-4 4-4 16 0 20" stroke="#fff" stroke-width="1.3" fill="none"/></svg>www.brindlecovenutrition.com.au</li>
  </ul>
</section>

<section class="card card--back" aria-label="Card back">
  <svg class="card__bands" viewBox="0 0 760 450" aria-hidden="true">
    <defs>
      <linearGradient id="swooshBack" x1="0" y1="0" x2="0" y2="1">
        <stop offset="0" stop-color="#8cc63f"/>
        <stop offset=".6" stop-color="#d6e61c"/>
        <stop offset="1" stop-color="#8cc63f"/>
      </linearGradient>
    </defs>
    <path d="M0,0 L150,0 C95,120 85,290 140,380 C170,414 260,416 760,408 L760,450 L0,450 Z" fill="#c9cbcd"/>
    <path d="M0,0 L138,0 C82,120 72,295 128,388 C160,424 260,426 760,418 L760,450 L0,450 Z" fill="url(#swooshBack)"/>
    <path d="M0,0 L60,0 C30,120 25,260 40,340 C20,250 5,120 0,60 Z" fill="#0a57a3"/>
    <path d="M0,428 C90,430 140,440 170,450 L0,450 Z" fill="#0b7cc8"/>
  </svg>

  <h2 class="appointment__title">APPOINTMENT</h2>
  <div class="field field--date">Date:</div>
  <div class="field field--time">Time:</div>

  <h3 class="location__title">Appointment Location</h3>
  <ul class="location__list">
    <li><span class="checkbox"></span>Fernhollow Medical Centre</li>
    <li><span class="checkbox"></span>North Kelby Health</li>
    <li><span class="checkbox"></span>Pinebrook Doctors Surgery</li>
    <li><span class="checkbox"></span>Ashcourt Medical</li>
  </ul>

  <div class="badge" role="img" aria-label="Registered Clinical Nutritionist badge"></div>
</section>

</body>
</html>
```